15th year anniversary programme cover

a front cover for my 15th year anniversary dance show programme cover

fun funky show programme cover we are basing the show on the velvet ringmaster film that is out at the cinema - circus based theme but don't want to see any clowns on the front

Target Market(s)

the general public

Logo Text

Bluebell Academy of Dance and Performing Arts Present The Moonlit Parade

Logo styles of interest
Abstract Logo
Font styles to use
Sans Serif

Colors

Designer to choose colors to be used in the design.

Requirements
Must have
• fun lively celebrating 15 years

```html
<!DOCTYPE html>
<html lang="en">
<head>
<meta charset="utf-8">
<title>Bluebell Academy – The Moonlit Parade Programme Cover</title>
<link href="https://fonts.googleapis.com/css2?family=Anton&family=Courgette&family=Oswald:wght@500&family=Poppins:wght@500;600;700&family=Roboto+Slab:wght@800&display=swap" rel="stylesheet">
<style>
  :root {
    --frame-pink: #ff4f9b;
    --cream: #f7e3bf;
    --cream-light: #fbecd0;
    --cream-deep: #efd7aa;
    --logo-pink: #f0479a;
    --plum: #8e1651;
    --hot-pink: #ec2f86;
    --ribbon-pink: #f64aa0;
    --ribbon-fold: #d8136a;
    --orange: #fca90c;
    --red: #ee3324;
    --yellow: #fbb323;
    --teal: #0fa39a;
    --white: #ffffff;
  }
  * { margin: 0; padding: 0; box-sizing: border-box; }
  html, body { width: 792px; height: 1200px; overflow: hidden; background: var(--white); }
  .canvas { position: relative; width: 792px; height: 1200px; background: var(--white); }

  .frame {
    position: absolute; left: 29px; top: 27px; width: 736px; height: 1144px;
    background: var(--frame-pink);
  }
  .cover {
    position: absolute; left: 59px; top: 57px; width: 676px; height: 958px;
    background: radial-gradient(ellipse at 50% 80%, var(--cream-light) 0%, var(--cream) 55%, var(--cream-deep) 100%);
    overflow: hidden;
  }
  .bunting {
    position: absolute; left: 0; top: 47px; width: 676px; height: 84px;
    background: linear-gradient(90deg, var(--yellow), var(--red), var(--yellow), var(--red));
    clip-path: polygon(0 0, 100% 10%, 100% 40%, 50% 100%, 0 40%);
    opacity: 0.85;
  }

  .brand { position: absolute; left: 0; top: 190px; width: 676px; text-align: center; color: var(--logo-pink); font-family: "Poppins", sans-serif; font-weight: 600; }
  .brand-name { font-size: 84px; line-height: 1; letter-spacing: 1px; }
  .brand-mark { display: inline-block; width: 22px; height: 22px; border-radius: 50%; background: var(--logo-pink); margin-right: 10px; vertical-align: middle; }
  .brand-sub { font-size: 13px; letter-spacing: 0.5px; margin-top: 18px; text-transform: uppercase; }

  .present {
    position: absolute; left: 202px; top: 419px; width: 273px; height: 60px;
    background: var(--plum); border-radius: 30px;
    color: var(--white); font-family: "Poppins", sans-serif; font-weight: 700;
    font-size: 32px; letter-spacing: 4px; text-align: center; line-height: 60px;
  }
  .show-title {
    position: absolute; left: 0; top: 488px; width: 676px; text-align: center;
    font-family: "Anton", sans-serif; font-size: 54px; line-height: 64px; letter-spacing: 2px;
    color: var(--hot-pink); text-shadow: -2px -2px 0 var(--white);
  }

  .ribbon { position: absolute; left: 0; top: 0; width: 676px; height: 958px; }
  .celebrating {
    position: absolute; left: 189px; top: 578px; width: 296px; height: 76px;
    color: var(--white); font-family: "Courgette", cursive; font-size: 44px;
    text-align: center; line-height: 76px;
  }
  .years {
    position: absolute; left: 133px; top: 677px; width: 407px; height: 91px;
    color: var(--white); font-family: "Roboto Slab", serif; font-weight: 800;
    font-size: 64px; letter-spacing: 6px; text-align: center; line-height: 91px;
  }

  .balloons { position: absolute; border-radius: 50% 50% 46% 46%; }
  .balloons-left { left: 20px; top: 560px; width: 130px; height: 196px;
    background: linear-gradient(160deg, var(--red) 0%, var(--yellow) 50%, var(--teal) 100%); }
  .balloons-right { left: 548px; top: 572px; width: 125px; height: 201px;
    background: linear-gradient(200deg, var(--red) 0%, var(--yellow) 50%, var(--teal) 100%); }

  .details {
    position: absolute; left: 0; top: 822px; width: 676px; text-align: center;
    font-family: "Oswald", sans-serif; font-weight: 500; font-size: 23px; line-height: 31px;
    letter-spacing: 2px; color: var(--plum); text-transform: uppercase;
  }

  .notes {
    position: absolute; left: 29px; top: 1038px; width: 736px;
    font-family: "Poppins", sans-serif; font-weight: 600; font-size: 18.5px; color: var(--white);
  }
  .notes p { position: absolute; left: 25px; white-space: nowrap; }
  .notes p:nth-child(2) { top: 47px; left: 26px; }
</style>
</head>
<body>
<div class="canvas">
  <div class="frame"></div>
  <div class="cover">
    <div class="bunting" role="img" aria-label="Festive bunting of red and yellow pennant flags"></div>

    <div class="brand">
      <div class="brand-name"><span class="brand-mark"></span>Bluebell</div>
      <div class="brand-sub">Academy of Dance and Performing Arts</div>
    </div>

    <div class="present">PRESENT</div>
    <h1 class="show-title">THE MOONLIT PARADE</h1>

    <div class="balloons balloons-left" role="img" aria-label="Cluster of red, yellow and teal balloons"></div>
    <div class="balloons balloons-right" role="img" aria-label="Cluster of red, yellow and teal balloons"></div>

    <svg class="ribbon" viewBox="0 0 676 958" aria-hidden="true">
      <polygon points="189,654 485,654 540,677 133,677" fill="var(--ribbon-fold)"/>
      <polygon points="189,654 330,677 133,677" fill="#b80f5c"/>
      <rect x="189" y="578" width="296" height="76" fill="var(--ribbon-pink)"/>
      <rect x="133" y="677" width="407" height="91" fill="var(--orange)"/>
      <ellipse cx="336" cy="782" rx="150" ry="8" fill="#d9c39b" opacity="0.6"/>
    </svg>
    <div class="celebrating">celebrating</div>
    <div class="years">15 YEARS</div>

    <div class="details">Lorel ipsum dolor sit amet esta di maria<br>nuno valencia</div>
  </div>

  <div class="notes">
    <p>Print Ready- A4 size- Fonts available- RGB MODE- CMYK MODE</p>
    <p>Please let me know any content you want to show in this banner</p>
  </div>
</div>
</body>
</html>
```